Morvela Aesthetic Doctor

I require an elegant, luxurious looking business card for my aesthetic business. I am a doctor and that will set me aside from competitors. I am planning to provide home and spa based treatments to clients with high expectations. I have attached my logo.

```html
<!DOCTYPE html>
<html lang="en">
<head>
<meta charset="utf-8">
<title>Morvela Aesthetic Doctor – Business Card</title>
<link rel="stylesheet" href="https://fonts.googleapis.com/css2?family=Roboto:wght@300;400;700&display=swap">
<style>
  :root {
    --page-bg: #e9ecef;
    --blue-light: #43a9e3;
    --blue-mid: #3180d0;
    --blue-deep: #2a6fc2;
    --sky-1: #d6eefa;
    --sky-2: #8ccbef;
    --sky-3: #4aa6df;
    --white: #ffffff;
    --text-soft: #e6f2fb;
  }
  * { box-sizing: border-box; margin: 0; padding: 0; }
  html, body {
    width: 1200px; height: 1200px; overflow: hidden;
    background: var(--page-bg);
    font-family: "Roboto", Arial, sans-serif;
  }
  .card {
    position: absolute; left: 145px;
    width: 910px; height: 520px;
    border-radius: 6px; overflow: hidden;
    box-shadow: 0 8px 24px rgba(0,0,0,.18);
  }
  /* Front */
  .card--front {
    top: 50px;
    background: linear-gradient(160deg, var(--blue-light) 0%, var(--blue-mid) 55%, var(--blue-deep) 100%);
    display: flex; flex-direction: column; align-items: center; justify-content: center;
    color: var(--white); text-align: center;
  }
  .brand { display: flex; align-items: center; gap: 28px; margin-bottom: 40px; }
  .brand__dot {
    width: 110px; height: 110px; border-radius: 50%;
    border: 3px solid var(--white);
  }
  .brand__name {
    font-weight: 300; color: var(--white); text-align: left;
    text-transform: uppercase; letter-spacing: 4px; line-height: 1.05;
  }
  .brand__name .line1 { display: block; font-size: 80px; }
  .brand__name .line2 { display: block; font-size: 34px; letter-spacing: 3px; }
  .services { font-size: 25px; font-weight: 300; line-height: 1.45; color: var(--text-soft); }
  /* Back */
  .card--back {
    top: 620px;
    background: linear-gradient(160deg, var(--blue-mid) 0%, var(--blue-deep) 100%);
  }
  .back__art { position: absolute; left: 0; top: 0; width: 520px; height: 520px; }
  .back__info {
    position: absolute; right: 60px; top: 48px;
    text-align: right; color: var(--white);
  }
  .back__info .brand__name .line1 { font-size: 64px; }
  .back__info .brand__name .line2 { font-size: 27px; }
  .back__info .brand__name { text-align: right; margin-bottom: 24px; }
  .doctor__name { font-size: 36px; font-weight: 700; }
  .doctor__post { font-size: 20px; font-weight: 700; margin-top: 4px; }
  .doctor__cred { font-size: 25px; font-weight: 300; line-height: 1.3; margin-top: 10px; }
  .contacts { list-style: none; margin-top: 30px; font-size: 25px; font-weight: 300; }
  .contacts li { display: flex; justify-content: flex-end; align-items: center; gap: 16px; margin-top: 6px; }
  .contacts svg { width: 24px; height: 24px; fill: none; stroke: var(--white); stroke-width: 1.8; }
</style>
</head>
<body>

<section class="card card--front">
  <div class="brand">
    <span class="brand__dot"></span>
    <span class="brand__name"><span class="line1">Morvela</span><span class="line2">Aesthetic Doctor</span></span>
  </div>
  <p class="services">
    Dermal injectables • Plasma facials • Microneedling<br>
    Skin boosters • Excessive sweating<br>
    Home and Spa Based Treatments
  </p>
</section>

<section class="card card--back">
  <svg class="back__art" viewBox="0 0 520 520" role="img" aria-label="Illustration area: flowing blue ribbon profile artwork on white">
    <defs>
      <linearGradient id="artTone" x1="0" y1="0" x2="1" y2="1">
        <stop offset="0" stop-color="#ffffff"/>
        <stop offset=".45" stop-color="#d6eefa"/>
        <stop offset="1" stop-color="#8ccbef"/>
      </linearGradient>
    </defs>
    <path d="M0 0 H400 C470 60 500 160 480 260 C470 320 430 380 370 420 C330 450 300 490 290 520 H0 Z" fill="url(#artTone)"/>
  </svg>

  <div class="back__info">
    <p class="brand__name"><span class="line1">Morvela</span><span class="line2">Aesthetic Doctor</span></p>
    <p class="doctor__name">Dr Elise Varnow</p>
    <p class="doctor__post">MRCPCH MD</p>
    <p class="doctor__cred">Australasian Diploma<br>of Aesthetic Medicine</p>
    <ul class="contacts">
      <li>0800 555 019
        <svg viewBox="0 0 24 24"><path d="M5 3h4l2 5-2.5 1.5a11 11 0 0 0 6 6L16 13l5 2v4a2 2 0 0 1-2 2A16 16 0 0 1 3 5a2 2 0 0 1 2-2z"/></svg>
      </li>
      <li>elise@morvela.co.nz
        <svg viewBox="0 0 24 24"><rect x="3" y="5" width="18" height="14" rx="1"/><path d="M3 6l9 7 9-7"/></svg>
      </li>
      <li>www.morvela.co.nz
        <svg viewBox="0 0 24 24"><circle cx="12" cy="12" r="9"/><path d="M3 12h18M12 3c3 3 3 15 0 18M12 3c-3 3-3 15 0 18"/></svg>
      </li>
    </ul>
  </div>
</section>

</body>
</html>
```